Wine label refresh

We are wanting to modify our Corran Hollow label to include a picture on it.
I have attached the pictures below which we would like on the label. They are of the Corran Hollow vineyard. I have also attached an example of another label with a picture on it that we like the style of.
Updates
Industry/Entity Type
Vineyard
Requirements
Must have
- The Corran Hollow text must stay the same but can be moved down. It still needs to be the same size though.
Marlborough Sauvignon Blanc should remain in the same font and roughly the same size.
Wine of New Zealand also must stay but could potentially be moved.
Nice to have
- It would be nice if we could keep the PM logo on the front label but feel free to experiment with where this goes.

```html
<!DOCTYPE html>
<html lang="en">
<head>
<meta charset="utf-8">
<title>Corran Hollow – Marlborough Sauvignon Blanc Label</title>
<link rel="stylesheet" href="https://fonts.googleapis.com/css2?family=Cormorant+SC:wght@500&family=Pinyon+Script&family=Lato:wght@300&display=swap">
<style>
  :root {
    --canvas-bg: #e6e6e6;
    --label-paper: #ffffff;
    --label-gold: #c9a36a;
    --label-green: #0f5a35;
    --script-gold: #b9955c;
    --detail-grey: #8a8a8a;
    --photo-light: #c3c7c6;
    --photo-deep: #6f8a55;
  }
  * { box-sizing: border-box; margin: 0; padding: 0; }
  html, body {
    width: 1200px;
    height: 900px;
    overflow: hidden;
    background: var(--canvas-bg);
  }
  .canvas {
    position: relative;
    width: 1200px;
    height: 900px;
  }
  .wine-label {
    position: absolute;
    left: 50%;
    top: 50%;
    width: 465px;
    height: 580px;
    transform: translate(-50%, -50%) scale(1.45);
  }
  .label-shape {
    position: absolute;
    inset: 0;
    width: 465px;
    height: 580px;
    overflow: visible;
  }
  .label-outline { fill: var(--label-paper); stroke: var(--label-gold); stroke-width: 8; }
  .label-rule { fill: none; stroke: var(--label-green); stroke-width: 2; }
  .label-content {
    position: absolute;
    inset: 0;
    text-align: center;
  }
  .label-content > * {
    position: absolute;
    left: 0;
    right: 0;
    line-height: 1;
  }
  .monogram {
    top: 62px;
    font-family: "Cormorant SC", serif;
    font-weight: 500;
    font-size: 40px;
    letter-spacing: 4px;
    color: var(--script-gold);
  }
  .vineyard-photo {
    left: 39px;
    right: auto;
    top: 137px;
    width: 388px;
    height: 196px;
    border-radius: 8px;
    background: linear-gradient(to bottom, var(--photo-light), var(--photo-deep));
  }
  .estate-name {
    top: 362px;
    font-family: "Cormorant SC", serif;
    font-weight: 500;
    font-size: 40px;
    letter-spacing: 2px;
    color: var(--label-green);
  }
  .varietal {
    top: 416px;
    font-family: "Pinyon Script", cursive;
    font-size: 26px;
    color: var(--script-gold);
  }
  .vintage {
    top: 450px;
    font-family: "Pinyon Script", cursive;
    font-size: 22px;
    color: var(--script-gold);
  }
  .origin {
    top: 494px;
    font-family: "Lato", sans-serif;
    font-weight: 300;
    font-size: 15px;
    letter-spacing: 0.5px;
    color: var(--detail-grey);
  }
  .volume-strength {
    top: 521px;
    font-family: "Lato", sans-serif;
    font-weight: 300;
    font-size: 14px;
    word-spacing: 6px;
    color: var(--detail-grey);
  }
</style>
</head>
<body>
  <main class="canvas">
    <section class="wine-label">
      <svg class="label-shape" viewBox="0 0 465 580" aria-hidden="true">
        <path class="label-outline" d="M0,135 A45,45 0 0 0 45,90 Q232,-60 420,90 A45,45 0 0 0 465,135 L465,490 A45,45 0 0 0 420,535 Q232,620 45,535 A45,45 0 0 0 0,490 Z"/>
        <path class="label-rule" transform="translate(232.5 290) scale(0.955) translate(-232.5 -290)" d="M0,135 A45,45 0 0 0 45,90 Q232,-60 420,90 A45,45 0 0 0 465,135 L465,490 A45,45 0 0 0 420,535 Q232,620 45,535 A45,45 0 0 0 0,490 Z"/>
      </svg>
      <div class="label-content">
        <div class="monogram">PM</div>
        <div class="vineyard-photo" role="img" aria-label="Photograph of the Corran Hollow vineyard"></div>
        <h1 class="estate-name">Corran Hollow</h1>
        <p class="varietal">Marlborough Sauvignon Blanc</p>
        <p class="vintage">2012</p>
        <p class="origin">NEW ZEALAND WINE</p>
        <p class="volume-strength">750ml 13% alc/vol</p>
      </div>
    </section>
  </main>
</body>
</html>
```